KVPLAX25

We want to make a full page advertisement that will be published in The Halvard magazine. It needs to be 8” x 10.75” high resolution. Our intention is to feature our upcoming attendance at KV-PLAX conference in Saratoga Springs, NY in April. More information about the show can be found at https://www.kv-plax.org/brenmoor-kv-plax-2025/. We want to showcase our rapid expansion and need for good quality people to join our team in the Northeast United States.

```html
<!DOCTYPE html>
<html lang="en">
<head>
<meta charset="utf-8">
<title>KV-PLAX 2025 – Bridgeton Geothermal</title>
<link href="https://fonts.googleapis.com/css2?family=Oswald:wght@600&family=Poppins:wght@400;500;600;700&display=swap" rel="stylesheet">
<style>
  :root {
    --red: #ec1c24;
    --black: #0a0a0a;
    --white: #ffffff;
    --green: #0f5a36;
    --blue: #1aa3dc;
    --yellow: #ffe14a;
    --photo-earth: #b49a74;
    --photo-sky: #5aa3dc;
  }
  * { margin: 0; padding: 0; box-sizing: border-box; }
  html, body { width: 924px; height: 1200px; overflow: hidden; background: var(--white); }
  body { position: relative; font-family: "Poppins", sans-serif; color: var(--black); }
  .shapes { position: absolute; inset: 0; width: 924px; height: 1200px; }
  .abs { position: absolute; }

  .brand { left: 140px; top: 72px; display: flex; align-items: center; gap: 12px; }
  .brand-mark { width: 58px; height: 58px; border-radius: 50%; background: var(--green); }
  .brand-name { font-weight: 700; font-size: 40px; color: var(--red); line-height: 1; }

  .event-name { left: 124px; top: 152px; font-family: "Oswald", sans-serif; font-weight: 600;
    font-size: 152px; line-height: 1; color: var(--red); letter-spacing: -1px; }
  .event-year { left: 124px; top: 287px; font-family: "Oswald", sans-serif; font-weight: 600;
    font-size: 152px; line-height: 1; color: var(--black); letter-spacing: -1px; }

  .venue-pin { left: 128px; top: 462px; width: 36px; height: 48px; }
  .venue { left: 176px; top: 452px; font-weight: 700; font-size: 25.5px; line-height: 31px; color: var(--green); }

  .intro { left: 128px; top: 533px; width: 420px; font-weight: 600; font-size: 15.5px; line-height: 20.5px; }

  .dates { left: 124px; top: 606px; font-weight: 700; font-size: 44px; line-height: 1; letter-spacing: -0.5px; }
  .dates .hl { color: var(--red); }

  .rule { height: 1.5px; background: var(--black); left: 126px; width: 411px; }
  .rule-1 { top: 668px; }
  .rule-2 { top: 774px; }

  .session-head { left: 128px; font-weight: 600; font-size: 14.5px; line-height: 18px; }
  .session-head .hl { color: var(--red); }
  .session-body { left: 126px; font-size: 14.8px; line-height: 18.5px; }
  .pre-head { top: 683px; }
  .pre-body { top: 725px; width: 340px; }
  .main-head { top: 793px; }
  .main-body { top: 838px; width: 290px; }

  .awards-title { left: 200px; width: 240px; top: 932px; text-align: center; font-weight: 700;
    font-size: 21px; color: var(--yellow); letter-spacing: 0.3px; }
  .awards-text { left: 128px; top: 967px; width: 425px; font-size: 11.3px; line-height: 13.7px; color: var(--white); }

  .contact { top: 1125px; color: var(--white); }
  .contact-label { font-weight: 600; font-size: 16px; line-height: 20px; }
  .contact-value { font-weight: 600; font-size: 12.8px; line-height: 18px; display: flex; align-items: center; gap: 4px; }
  .contact-value svg { width: 13px; height: 13px; }
  .contact-call { left: 68px; }
  .contact-mail { left: 211px; }
  .contact-web { left: 397px; }
</style>
</head>
<body>
  <svg class="shapes" viewBox="0 0 924 1200" aria-hidden="false">
    <defs>
      <linearGradient id="grad-rig" x1="0" y1="0" x2="0" y2="1">
        <stop offset="0" stop-color="#5a5a5a"/>
        <stop offset="0.55" stop-color="#8a8a86"/>
        <stop offset="1" stop-color="#b7b1a6"/>
      </linearGradient>
      <linearGradient id="grad-sky" x1="0" y1="0" x2="0" y2="1">
        <stop offset="0" stop-color="#4d9be0"/>
        <stop offset="0.6" stop-color="#6f9d5a"/>
        <stop offset="1" stop-color="#a48a6c"/>
      </linearGradient>
      <linearGradient id="grad-site" x1="0" y1="0" x2="1" y2="1">
        <stop offset="0" stop-color="#5d5d4e"/>
        <stop offset="0.5" stop-color="#b88e3a"/>
        <stop offset="1" stop-color="#c9a54a"/>
      </linearGradient>
      <linearGradient id="grad-trench" x1="0" y1="0" x2="0" y2="1">
        <stop offset="0" stop-color="#a07c5c"/>
        <stop offset="1" stop-color="#cdb799"/>
      </linearGradient>
    </defs>
    <polygon class="side-band" points="0,0 126,0 0,593" fill="var(--red)"/>
    <polygon class="edge-band" points="905,0 924,0 924,1101 760,1101" fill="var(--black)"/>
    <polygon class="awards-band" points="105,919 722,919 700,1097 67,1097" fill="var(--red)"/>
    <rect class="footer-band" x="0" y="1101" width="924" height="99" fill="var(--black)"/>

    <polygon role="img" aria-label="Photo: crew member beside a yellow drilling rig on a job site" points="669,91 924,91 924,230 880,366 601,366" fill="url(#grad-site)"/>
    <polygon role="img" aria-label="Photo: two red drilling rigs on trucks under a blue sky" points="667,370 924,370 924,500 847,634 571,634" fill="url(#grad-sky)"/>
    <polygon role="img" aria-label="Photo: geothermal loop pipes laid in an earth trench" points="656,639 912,639 912,700 841,911 562,911" fill="url(#grad-trench)"/>
    <polygon role="img" aria-label="Photo: red drilling rig truck and equipment at a wooded site" points="700,919 924,919 924,1200 575,1200 610,1101" fill="url(#grad-rig)"/>

    <g class="pushpins" fill="var(--black)">
      <circle cx="157" cy="942" r="6"/><rect x="155" y="947" width="4" height="8"/>
      <circle cx="491" cy="942" r="6"/><rect x="489" y="947" width="4" height="8"/>
    </g>
  </svg>

  <div class="brand abs">
    <span class="brand-mark"></span>
    <span class="brand-name">Bridgeton</span>
  </div>

  <div class="event-name abs">KV-PLAX</div>
  <div class="event-year abs">2025</div>

  <svg class="venue-pin abs" viewBox="0 0 36 48" aria-hidden="true">
    <path d="M18 3a11 11 0 0 0-11 11c0 8 11 20 11 20s11-12 11-20A11 11 0 0 0 18 3z" fill="none" stroke="var(--red)" stroke-width="4"/>
    <circle cx="18" cy="14" r="4" fill="var(--red)"/>
    <ellipse cx="18" cy="40" rx="15" ry="5" fill="none" stroke="var(--red)" stroke-width="3"/>
  </svg>
  <div class="venue abs">BRENMOOR SPRINGS GRAND<br>AND CITY CENTER</div>

  <p class="intro abs">The annual conference, spanning over two action-packed days, is a must attend event. for anyone in the geothermal industry.</p>

  <div class="dates abs"><span class="hl">22-24</span> APRIL 2025</div>

  <div class="rule rule-1 abs"></div>
  <div class="session-head pre-head abs"><span class="hl">PRE CONFERENCE ACTIVITIES an</span><br>TUESDAY, <span class="hl">APRIL 22</span> EARTH DAY</div>
  <p class="session-body pre-body abs">Pre-confierenice activities inc a Drilling Demonstration Geothermal Site Tours.</p>

  <div class="rule rule-2 abs"></div>
  <div class="session-head main-head abs"><span class="hl">KV-PLAX 2025 -</span><br>WEDNESDAY, <span class="hl">APRIL 23 and</span> THURSDAY, <span class="hl">APRIL 24</span></div>
  <p class="session-body main-body abs">Two full days of education, exhibitor networking, annual dinner and Top Job Awards.</p>

  <h2 class="awards-title abs">TOP JOBS</h2>
  <p class="awards-text abs">Top Job awards has been an integral part of the KV-PLAX annual conference since its inception in 2014. Its objective is to highlight and recognize the incredible skill, talent, and creative imagination that exists in geothermal system designers and installers. We will be recognizing and awarding three winners, one each, in the categories of Residential, Commercial and Drilling.</p>

  <div class="contact contact-call abs">
    <div class="contact-label">Call Us</div>
    <div class="contact-value"><svg viewBox="0 0 16 16"><path d="M3 1l3 3-2 2c1 2 3 4 5 5l2-2 3 3-2 3C7 15 1 9 1 3z" fill="var(--yellow)"/></svg>1-866-555-0142</div>
  </div>
  <div class="contact contact-mail abs">
    <div class="contact-label">Contact Us</div>
    <div class="contact-value"><svg viewBox="0 0 16 16"><rect x="1" y="3" width="14" height="10" fill="var(--yellow)"/><path d="M1 3l7 6 7-6" fill="none" stroke="var(--black)" stroke-width="1.2"/></svg>info@bridgetonwells.com</div>
  </div>
  <div class="contact contact-web abs">
    <div class="contact-label">Visit Us</div>
    <div class="contact-value"><svg viewBox="0 0 16 16"><circle cx="8" cy="8" r="7" fill="var(--yellow)"/><path d="M1 8h14M8 1c-4 4-4 10 0 14M8 1c4 4 4 10 0 14" fill="none" stroke="var(--black)" stroke-width="0.9"/></svg>www.bridgetonwells.com</div>
  </div>
</body>
</html>
```